We need a new business card that reflects who we are. Professional, classy, modern, and service ori

We need a business card design for a window coverings design company in Kansas City called Bright Lane Interiors. We offer professional, modern, and high quality window covering products. We are looking to portray an image of a big, national franchise. We are a 5 location (with showrooms) business with 10 professional designers and 4 professional installers. These cards will be used with Thank you cards, given to realtors, and asked for referrals with.

Target Market(s)

Kansas City

Industry/Entity Type

Business

Contact Information for Business Card

We would like our card to look clean and simple on the front, featuring our logo and Marlow Fenwick's. Our designers' phone numbers and emails should be displayed as well as their title.

Font styles to use
Sans Serif

Colors

Designer to choose colors to be used in the design.

Requirements
Must have
• Front - Logos, name, phone number, email address
• Back - Showroom locations, social media? Appt date/time?
Nice to have
• I would like a clean and modern look (not contemporary. I like a white background, but I am open to ideas. Looking for a "National chain" look for a small business.
Should not have
• Too much busyness.

```html
<!DOCTYPE html>
<html lang="en">
<head>
<meta charset="utf-8">
<title>Bright Lane Interiors – Business Card</title>
<link href="https://fonts.googleapis.com/css2?family=Sorts+Mill+Goudy&family=Libre+Baskerville:wght@700&family=Roboto:wght@400&family=Arimo:ital@1&display=swap" rel="stylesheet">
<style>
  :root{
    --backdrop:#7a6350;
    --card:#ffffff;
    --red:#c83f45;
    --grey:#9a9ea3;
    --ink:#1d1d1d;
    --orange:#ee8527;
    --slate:#5c6a78;
    --blue:#3b5998;
    --sky:#1da1f2;
    --link:#0e76a8;
    --rose:#dd4b39;
  }
  *{margin:0;padding:0;box-sizing:border-box}
  html,body{width:900px;height:1200px;overflow:hidden}
  body{background:var(--backdrop);position:relative;font-family:"Roboto",Arial,sans-serif;color:var(--ink)}
  .card{position:absolute;left:88px;width:732px;height:428px;background:var(--card);border-radius:22px;overflow:hidden;box-shadow:0 6px 14px rgba(0,0,0,.35)}
  .card--front{top:137px;background:linear-gradient(180deg,#fff 0%,#fff 55%,#f1f1f1 100%)}
  .card--back{top:633px}
  .shapes{position:absolute;inset:0}
  .abs{position:absolute}

  .brand{display:flex;align-items:center;gap:10px}
  .brand__mark{width:22px;height:22px;background:var(--red)}
  .brand__name{font-family:"Sorts Mill Goudy",Georgia,serif;font-size:31px;color:var(--ink);white-space:nowrap;letter-spacing:.2px}
  .brand__tagline{font-family:"Sorts Mill Goudy",Georgia,serif;font-size:18.5px;color:var(--ink);white-space:nowrap}

  .brand--back .brand__mark{width:18px;height:18px}
  .brand--back .brand__name{font-size:24px}
  .brand__tagline--back{font-size:14px;margin-top:8px}

  .person__name{font-family:"Libre Baskerville",Georgia,serif;font-weight:700;font-size:27px;color:var(--ink);text-align:right}
  .person__title{font-family:"Sorts Mill Goudy",Georgia,serif;font-size:18px;color:var(--red);text-align:right;margin-top:6px}

  .contact{display:flex;align-items:center;gap:10px;font-size:18px;white-space:nowrap}
  .contact__icon{width:22px;height:22px;border-radius:50%;background:var(--red);display:flex;align-items:center;justify-content:center}

  .partner__name{font-family:"Roboto",Arial,sans-serif;font-size:24px;color:var(--slate);text-align:center;line-height:1.05}

  .slogan{font-family:"Arimo",Arial,sans-serif;font-style:italic;font-size:16.5px;color:#fff;white-space:nowrap}

  .field{font-family:"Sorts Mill Goudy",Georgia,serif;font-size:16px;color:var(--ink)}
  .rule{position:absolute;height:2px;background:var(--ink)}

  .loc-label{font-size:15px;color:#fff;transform:rotate(-90deg);transform-origin:left top;white-space:nowrap}
  .address{display:flex;align-items:flex-start;gap:8px;color:#fff;font-size:16px;line-height:20px}
  .address__bar{width:1.5px;height:40px;background:#fff;margin-left:4px}
  .social{position:absolute;width:32px;height:32px}
</style>
</head>
<body>

<section class="card card--front" aria-label="Business card front">
  <svg class="shapes" width="732" height="428" viewBox="0 0 732 428">
    <polygon points="462,0 732,0 732,40 482,40" fill="var(--red)"/>
    <polygon points="622,414 640,414 732,414 732,428 648,428" fill="var(--grey)"/>
    <polygon points="0,386 624,386 648,414 0,414" fill="var(--red)"/>
    <line x1="42" y1="247" x2="542" y2="247" stroke="var(--red)" stroke-width="1.5"/>
    <circle cx="609" cy="248" r="52" fill="var(--orange)"/>
  </svg>

  <div class="abs" style="left:42px;top:150px">
    <div class="brand"><span class="brand__mark"></span><span class="brand__name">Bright Lane Interiors</span></div>
    <div class="brand__tagline" style="margin-top:6px">Blinds, Shades, Shutters, Draperies &amp; Decor</div>
  </div>

  <div class="abs" style="right:43px;top:80px">
    <div class="person__name">Daniel Carver</div>
    <div class="person__title">Managing Director</div>
  </div>

  <div class="abs" style="left:42px;top:267px">
    <div class="contact">
      <span class="contact__icon"><svg width="12" height="12" viewBox="0 0 24 24"><path fill="#fff" d="M6.6 10.8a15.1 15.1 0 006.6 6.6l2.2-2.2c.3-.3.7-.4 1-.2 1.1.4 2.3.6 3.6.6.6 0 1 .4 1 1V20c0 .6-.4 1-1 1A17 17 0 013 4c0-.6.4-1 1-1h3.5c.6 0 1 .4 1 1 0 1.3.2 2.5.6 3.6.1.3 0 .7-.2 1z"/></svg></span>
      <span>+61 3 9000 4127</span>
    </div>
    <div class="contact" style="margin-top:6px">
      <span class="contact__icon"><svg width="12" height="10" viewBox="0 0 24 18"><rect x="1" y="1" width="22" height="16" fill="none" stroke="#fff" stroke-width="2.5"/><polyline points="1,1 12,10 23,1" fill="none" stroke="#fff" stroke-width="2.5"/></svg></span>
      <span>info@brightlaneinteriors.com</span>
    </div>
  </div>

  <div class="abs partner__name" style="left:520px;top:313px;width:178px">Marlow Fenwick<br>Gallery</div>

  <div class="abs slogan" style="left:37px;top:391px">Professional, modern, and high quality window covering products</div>
</section>

<section class="card card--back" aria-label="Business card back">
  <svg class="shapes" width="732" height="428" viewBox="0 0 732 428">
    <rect x="0" y="242" width="57" height="186" fill="var(--grey)"/>
    <rect x="57" y="242" width="675" height="186" fill="var(--red)"/>
    <polygon points="497,429 550,380 732,380 732,429" fill="#fff"/>
  </svg>

  <div class="abs" style="left:42px;top:138px;width:280px">
    <div class="brand brand--back"><span class="brand__mark"></span><span class="brand__name">Bright Lane Interiors</span></div>
    <div class="brand__tagline brand__tagline--back">Blinds, Shades, Shutters, Draperies &amp; Decor</div>
  </div>

  <div class="abs field" style="left:344px;top:44px">Name</div>
  <div class="rule" style="left:344px;top:69px;width:341px"></div>

  <div class="abs field" style="left:344px;top:106px">Time</div>
  <div class="abs field" style="left:499px;top:106px">:</div>
  <div class="abs field" style="left:628px;top:108px;font-size:14px">AM / PM</div>
  <div class="rule" style="left:344px;top:131px;width:154px"></div>
  <div class="rule" style="left:505px;top:131px;width:180px"></div>

  <div class="abs field" style="left:344px;top:166px">Date</div>
  <div class="abs field" style="left:486px;top:166px">/</div>
  <div class="abs field" style="left:590px;top:166px">/</div>
  <div class="rule" style="left:344px;top:191px;width:140px"></div>
  <div class="rule" style="left:490px;top:191px;width:98px"></div>
  <div class="rule" style="left:594px;top:191px;width:91px"></div>

  <div class="abs loc-label" style="left:20px;top:398px">Office Locations</div>

  <div class="abs" style="left:88px;top:262px">
    <div class="address"><svg width="12" height="18" viewBox="0 0 12 18"><path fill="#fff" d="M6 0a6 6 0 016 6c0 4.5-6 12-6 12S0 10.5 0 6a6 6 0 016-6zm0 3.5a2.5 2.5 0 100 5 2.5 2.5 0 000-5z"/></svg><span class="address__bar"></span><span>240 Harbour Row, Toronto<br>ON M5J 2K8</span></div>
  </div>
  <div class="abs" style="left:88px;top:309px">
    <div class="address"><svg width="12" height="18" viewBox="0 0 12 18"><path fill="#fff" d="M6 0a6 6 0 016 6c0 4.5-6 12-6 12S0 10.5 0 6a6 6 0 016-6zm0 3.5a2.5 2.5 0 100 5 2.5 2.5 0 000-5z"/></svg><span class="address__bar"></span><span>18 Orchard Lane, #140<br>Salinas, CA 93905</span></div>
  </div>
  <div class="abs" style="left:88px;top:358px">
    <div class="address"><svg width="12" height="18" viewBox="0 0 12 18"><path fill="#fff" d="M6 0a6 6 0 016 6c0 4.5-6 12-6 12S0 10.5 0 6a6 6 0 016-6zm0 3.5a2.5 2.5 0 100 5 2.5 2.5 0 000-5z"/></svg><span class="address__bar"></span><span>3320-52b avenue<br>leduc, alberta t9e 2k7</span></div>
  </div>
  <div class="abs" style="left:444px;top:264px">
    <div class="address"><svg width="12" height="18" viewBox="0 0 12 18"><path fill="#fff" d="M6 0a6 6 0 016 6c0 4.5-6 12-6 12S0 10.5 0 6a6 6 0 016-6zm0 3.5a2.5 2.5 0 100 5 2.5 2.5 0 000-5z"/></svg><span class="address__bar"></span><span>4, 12 Kestrel Road<br>Bayswater VIC 3153</span></div>
  </div>
  <div class="abs" style="left:444px;top:313px">
    <div class="address"><svg width="12" height="18" viewBox="0 0 12 18"><path fill="#fff" d="M6 0a6 6 0 016 6c0 4.5-6 12-6 12S0 10.5 0 6a6 6 0 016-6zm0 3.5a2.5 2.5 0 100 5 2.5 2.5 0 000-5z"/></svg><span class="address__bar"></span><span>10920 - 87 Ave. Edmonton<br>AB, Canada. T6G 1A4</span></div>
  </div>

  <span class="social" style="left:559px;top:390px;background:var(--blue)"></span>
  <span class="social" style="left:596px;top:390px;background:var(--sky)"></span>
  <span class="social" style="left:632px;top:390px;background:var(--link)"></span>
  <span class="social" style="left:669px;top:390px;background:var(--rose)"></span>
</section>

</body>
</html>
```